Letterhead to coordinate with business card

I am needing a docx template and print file for a letterhead to co-ordinate with my newly designed logo and business card.

```html
<!DOCTYPE html>
<html lang="en">
<head>
<meta charset="utf-8">
<title>Harbourline Plan Services — Letterhead</title>
<link rel="stylesheet" href="https://fonts.googleapis.com/css2?family=Arimo:wght@400;700&family=Questrial&display=swap">
<style>
  :root {
    --backdrop: #adabac;
    --paper: #ffffff;
    --navy: #2f3440;
    --teal: #00807f;
    --berry: #a83266;
    --ink: #4a4a4a;
    --ink-dark: #3b3b3b;
  }
  html, body {
    margin: 0;
    width: 1200px;
    height: 934px;
    overflow: hidden;
    background: var(--backdrop);
  }
  .letterhead {
    position: absolute;
    left: 322px;
    top: 74px;
    width: 556px;
    height: 785px;
    background: var(--paper);
    box-shadow: 2px 2px 4px rgba(0,0,0,0.35);
    font-family: "Arimo", Arial, sans-serif;
    color: var(--ink);
  }
  .header-band {
    position: absolute;
    left: 0;
    top: 0;
    width: 556px;
    height: 90px;
    display: block;
  }
  .brand {
    position: absolute;
    left: 0;
    top: 56px;
    width: 556px;
    text-align: center;
  }
  .brand-mark {
    width: 44px;
    height: 44px;
    margin: 0 auto;
    background: var(--berry);
  }
  .brand-name {
    margin-top: 10px;
    font-size: 15px;
    font-weight: 700;
    letter-spacing: 0.5px;
    color: var(--berry);
  }
  .salutation {
    position: absolute;
    left: 50px;
    top: 240px;
    margin: 0;
    font-family: "Questrial", "Century Gothic", sans-serif;
    font-weight: 700;
    font-size: 13px;
    color: var(--ink);
  }
  .letter-body {
    position: absolute;
    left: 50px;
    top: 277px;
    width: 456px;
    font-size: 9.5px;
    line-height: 11.4px;
  }
  .letter-body p {
    margin: 0 0 10px;
  }
  .closing {
    position: absolute;
    left: 50px;
    top: 514px;
    margin: 0;
    font-family: "Questrial", "Century Gothic", sans-serif;
    font-weight: 700;
    font-size: 7.5px;
    color: var(--ink-dark);
  }
  .signature {
    position: absolute;
    left: 50px;
    top: 547px;
    width: 91px;
    height: 27px;
    background: #e4e4e4;
  }
  .footer-address {
    position: absolute;
    left: 69px;
    top: 741px;
    width: 416px;
    display: flex;
    align-items: center;
    gap: 4px;
    font-size: 9.6px;
    color: var(--ink-dark);
  }
  .footer-address .rule {
    flex: 1;
    height: 1px;
    background: var(--teal);
  }
  .footer-contacts {
    position: absolute;
    left: 69px;
    top: 757px;
    display: flex;
    gap: 8px;
    font-size: 9.6px;
    white-space: nowrap;
    color: var(--ink-dark);
  }
  .contact {
    display: flex;
    align-items: center;
    gap: 4px;
  }
  .contact svg {
    width: 8px;
    height: 8px;
  }
</style>
</head>
<body>
  <article class="letterhead">
    <svg class="header-band" viewBox="0 0 556 90" preserveAspectRatio="none" role="img" aria-label="Decorative header band in navy, teal and berry tones">
      <defs>
        <linearGradient id="band-tone" x1="0" y1="0" x2="1" y2="1">
          <stop offset="0" stop-color="var(--navy)"/>
          <stop offset="0.55" stop-color="var(--teal)"/>
          <stop offset="1" stop-color="var(--berry)"/>
        </linearGradient>
      </defs>
      <path d="M0 0 H556 V87 Q278 -7 0 87 Z" fill="url(#band-tone)"/>
    </svg>

    <div class="brand">
      <div class="brand-mark"></div>
      <div class="brand-name">Harbourline Plan Services</div>
    </div>

    <h1 class="salutation">Dear Mr. Carter,</h1>

    <div class="letter-body">
      <p>Lorem ipsum dolor sit amet, consectetuer adipiscing elit, sed diam nonmmy nibh euismod tincidunt ut laor eet dolore magna aliquam erat volutpat. Ut wisi enim ad minim veniam, quis nostrud exerci tationmcorper suscipit lobortis nisl ut aliquip ex ea commodo consequat. Duis autem vel eum iriure dolor in hendrerit in vulputate velit esse molestie consequat, vel illum dolore eu feugiat</p>
      <p>Rorem ipsum dolor sit amet, consectetuer adipiscing elit, sed diam nonmmy nibh euismod tincidunt ut laor eet dolore magna aliquam erat volutpat. Ut wisi enim ad minim veniam, quis nostrud exerci tationmcorper suscipit lobortis nisl ut aliquip ex ea commodo consequat. Duis autem vel eum iriure dolor in hendrerit in vulputate velit esse molest</p>
      <p>Dorem ipsum dolor sit amet, consectetuer adipiscing elit, sed diam nonmmy nibh euismod tincidunt ut laor eet dolore magna aliquam erat volutpat. Ut wisi enim ad minim veniam, quis nostrud exerci tationmcorper suscipit lobortis nisl ut aliquip ex ea commodo consequat. Duis autem vel eum iriure dolor in hendrerit in suscipit lobortis nisl ut aliquip ex ea commodo consequat. Duis autem vel eum iriure dolor in hendrerit in vulputate velit esse molestie consequat, vel illum</p>
      <p>Sorem ipsum dolor sit amet, consectetuer adipiscing elit, sed diam nonmmy nibh euismod tincidunt ut laor eet dolore magna aliquam erat volutpat. Ut wisi enim ad minim veniam, quis nostrud exerci tationmcorper suscipit lobortis nisl ut aliquip ex ea commodo consequat. Duis autem vel eum iriure dolor in</p>
    </div>

    <p class="closing">Sincerely,</p>
    <div class="signature" role="img" aria-label="Handwritten signature of the sender"></div>

    <footer>
      <div class="footer-address">
        <span class="rule"></span>
        <span>PO Box 42, Lakeside NSW 2000</span>
        <span class="rule"></span>
      </div>
      <div class="footer-contacts">
        <span class="contact">
          <svg viewBox="0 0 10 10" aria-hidden="true"><circle cx="5" cy="5" r="5" fill="var(--teal)"/><path d="M3.2 2.6 L4.2 2.4 L4.6 3.8 L4 4.2 Q4.6 5.6 5.8 6 L6.2 5.4 L7.6 5.8 L7.4 6.8 Q4 7 3.2 2.6 Z" fill="#fff"/></svg>
          0400 000 123
        </span>
        <span class="contact">
          <svg viewBox="0 0 10 10" aria-hidden="true"><circle cx="5" cy="5" r="5" fill="var(--teal)"/><rect x="2.6" y="3.3" width="4.8" height="3.4" fill="#fff"/><path d="M2.6 3.3 L5 5.2 L7.4 3.3" stroke="var(--teal)" stroke-width="0.6" fill="none"/></svg>
          hello@harbourlineplans.com.au
        </span>
        <span class="contact">
          <svg viewBox="0 0 10 10" aria-hidden="true"><circle cx="5" cy="5" r="5" fill="var(--teal)"/><circle cx="5" cy="5" r="2.6" fill="none" stroke="#fff" stroke-width="0.7"/><path d="M2.4 5 H7.6 M5 2.4 V7.6" stroke="#fff" stroke-width="0.6"/></svg>
          www.harbourlineplans.com.au
        </span>
      </div>
    </footer>
  </article>
</body>
</html>
```